Cask Annals, a definitive reference book on port

My husband has just finished writing a big book on Vintage Port. We need a hardcover book flap design for this book that is impressively huge. It's taken 10 years to research and write. It's 650 pages, interior is A4, exterior 4mm larger, and weighs nearly 3 kilos. It's a special book for people in the wine and port industry, as well as for someone who loves to drink Vintage Port. It can be a beautiful coffeetable book too.

The book is mainly about port and its declared vintages. It's also about the history of port, who drank it, when, how, where, who bought it, for how much, and the port houses are also described in detail.

The wine expert Tobias Quellmore wrote a book about vintage wine in 2002, and my husband would like to have a similar cover for his book. (A photo attached in files). I've attached other photos to give the designers an idea of the look and feel of the 'port culture', as well as photos of the typeface that my husband will be using for the inside hardcover.

Target Market(s)

Wine and port industry. Wine aficionados.

Industry/Entity Type

Winery

Font styles to use
Sans Serif
Script

Colors
ec1f27
1b1b1b
474747
333333
5c5c5c
faa54b

Requirements
Must have
• Book Cover must have Title: "Cask Annals" and "R. K. P. Holloway" (files attached to show proper typeface). One of the files is a flap jacket book cover that my husband designed himself. We're looking for more design ideas, and that pdf is a close winner to what he wants.
Nice to have
• illustration or painting of port glasses, or grapes, or similar. Dark colors, especially port wine, deep red wine colors. Gold writing, black writing, with red/berry/maroon accents. Luxury, elegance, has a masculine edge, traditional, but not too old-school and boring (like grandpa). Textures that are including with the culture of drinking vintage port are leather, velvet, cigar, wood, marble, winter, fireplaces. This sounds quite heavy, but it also should be simple and clean. I hope this isn't too confusing. Thanks!
Should not have
• Bright colors, playfulness.

```html
<!DOCTYPE html>
<html lang="en">
<head>
<meta charset="utf-8">
<title>Cask Annals – Book Jacket</title>
<link href="https://fonts.googleapis.com/css2?family=Open+Sans:wght@700&family=Righteous&family=Marcellus+SC&family=Playball&display=swap" rel="stylesheet">
<style>
  :root {
    --jacket-red: #d9141f;
    --jacket-red-light: #e42630;
    --jacket-red-dark: #c10f19;
    --spine-black: #1b1b1b;
    --gold: #faa54b;
    --wine-dark: #3a0a10;
    --wine-mid: #7a1420;
  }
  * { margin: 0; padding: 0; box-sizing: border-box; }
  html, body { width: 1200px; height: 780px; overflow: hidden; background: var(--jacket-red); }
  .jacket {
    position: relative;
    width: 1200px;
    height: 780px;
    overflow: hidden;
    background:
      radial-gradient(ellipse at 30% 40%, var(--jacket-red-light) 0%, transparent 60%),
      radial-gradient(ellipse at 80% 70%, var(--jacket-red-light) 0%, transparent 55%),
      linear-gradient(160deg, var(--jacket-red) 0%, var(--jacket-red-dark) 100%);
  }
  .spine {
    position: absolute;
    left: 549px;
    top: 0;
    width: 96px;
    height: 780px;
    background: var(--spine-black);
  }
  .spine-title, .spine-author {
    position: absolute;
    left: 50%;
    transform: translateX(-50%);
    writing-mode: vertical-rl;
    font-family: "Open Sans", sans-serif;
    font-weight: 700;
    color: var(--gold);
    font-size: 40px;
    line-height: 1;
    letter-spacing: -0.5px;
    white-space: nowrap;
  }
  .spine-title { top: 35px; letter-spacing: 2px; }
  .spine-author { top: 428px; }
  .front-cover {
    position: absolute;
    left: 645px;
    top: 0;
    width: 555px;
    height: 780px;
  }
  .cover-title {
    position: absolute;
    top: 112px;
    left: 0;
    width: 100%;
    text-align: center;
    font-family: "Righteous", sans-serif;
    font-weight: 400;
    color: var(--jacket-red);
    -webkit-text-stroke: 2.5px var(--gold);
    line-height: 1;
    padding-left: 14px;
  }
  .cover-title .title-line-1 { display: block; font-size: 68px; letter-spacing: 4px; }
  .cover-title .title-line-2 { display: block; font-size: 68px; letter-spacing: 16px; margin-top: 18px; margin-right: -16px; }
  .cover-subtitle {
    position: absolute;
    top: 266px;
    left: 0;
    width: 100%;
    text-align: center;
    font-family: "Marcellus SC", serif;
    font-size: 18px;
    line-height: 23px;
    color: var(--gold);
    padding-left: 30px;
  }
  .cover-illustration {
    position: absolute;
    left: 207px;
    top: 355px;
    width: 167px;
    height: 224px;
    border-radius: 6px;
    background: linear-gradient(135deg, var(--wine-mid) 0%, var(--wine-dark) 100%);
  }
  .cover-author {
    position: absolute;
    top: 592px;
    left: 0;
    width: 100%;
    text-align: center;
    font-family: "Playball", cursive;
    font-size: 52px;
    letter-spacing: 2px;
    line-height: 1.1;
    color: var(--gold);
    padding-left: 14px;
    white-space: nowrap;
  }
</style>
</head>
<body>
  <div class="jacket">
    <section class="back-cover" aria-label="Back cover"></section>

    <section class="spine">
      <div class="spine-title">CASK ANNALS</div>
      <div class="spine-author">R. K. P. Holloway</div>
    </section>

    <section class="front-cover">
      <h1 class="cover-title">
        <span class="title-line-1">CASK</span>
        <span class="title-line-2">ANNALS</span>
      </h1>
      <p class="cover-subtitle">
        The Record of Declared Ports,<br>
        Across the Centuries,<br>
        Documented and Complete
      </p>
      <div class="cover-illustration" role="img" aria-label="Illustration of a port bottle, a filled wine glass, a bunch of dark grapes and a cork"></div>
      <p class="cover-author">R. K. P. Holloway</p>
    </section>
  </div>
</body>
</html>
```